Business Card Design

I would like a new business card design for an accounting firm that specializes in resolving clients tax problems. I want the card to give the impression that we are not your typical stodgy accounting firm, but at the same time we will get the job done.
Industry/Entity Type
Business
Contact Information for Business Card
Dorian T Welsby
Certified Public Accountant
38-27 52nd Street
Sunnyside, NY 11287
Tel: (718) 555-0142
Fax: (888) 555-0199
e-mail: dtwthecpa@ledgerpost.com
website: harborfilingreliefexperts.com

```html
<!DOCTYPE html>
<html lang="en">
<head>
<meta charset="utf-8">
<title>Dorian T Welsby, CPA: Business Card</title>
<link rel="stylesheet" href="https://fonts.googleapis.com/css2?family=Marcellus+SC&display=swap">
<style>
  :root {
    --page: #0b0b0d;
    --paper: #dcdcdc;
    --paper-monogram: #e4e4e4;
    --navy: #1b3590;
    --band: #1a3a9c;
    --band-monogram: #1d3d93;
    --ink-grey: #6b6b6b;
    --ink-white: #ffffff;
    --ink-sky: #6f93f0;
  }
  * { margin: 0; padding: 0; box-sizing: border-box; }
  html, body { width: 1200px; height: 818px; overflow: hidden; background: var(--page); }
  body {
    font-family: "Marcellus SC", "Optima", serif;
    display: flex; align-items: center; justify-content: center; gap: 40px;
  }
  .card {
    position: relative; width: 560px; height: 320px; overflow: hidden;
    box-shadow: 0 10px 30px rgba(0,0,0,.6);
  }
  .monogram-area { position: absolute; border-radius: 4px; }

  /* Front */
  .card-front { background: var(--paper); }
  .card-front .monogram-area { background: var(--paper-monogram); left: 34px; top: 22px; width: 250px; height: 142px; }
  .identity { position: absolute; right: 28px; text-align: right; }
  .card-front .identity { top: 112px; }
  .identity-name { font-size: 30px; color: var(--navy); line-height: 1; }
  .identity-title { font-size: 13.5px; color: var(--ink-grey); letter-spacing: 1px; margin-top: 4px; }
  .rule { position: absolute; left: 0; right: 0; top: 176px; height: 3px; background: var(--band); }
  .contact-band {
    position: absolute; left: 0; right: 0; top: 184px; bottom: 0; background: var(--band);
    color: var(--ink-white); line-height: 1.45;
  }
  .contact-online { position: absolute; left: 255px; top: 12px; font-size: 15px; }
  .contact-address { position: absolute; left: 22px; bottom: 16px; font-size: 16px; }
  .contact-address .indent { padding-left: 14px; }

  /* Back */
  .card-back { background: var(--band); }
  .card-back .monogram-area { background: var(--band-monogram); left: 70px; top: 120px; width: 250px; height: 176px; }
  .card-back .identity { bottom: 48px; }
  .card-back .identity-name { color: var(--ink-white); font-size: 34px; }
  .card-back .identity-title { color: var(--ink-sky); font-size: 15px; }
</style>
</head>
<body>
  <section class="card card-front" aria-label="Business card front">
    <div class="monogram-area" role="img" aria-label="Faint initials monogram watermark"></div>
    <div class="identity">
      <div class="identity-name">Dorian T Welsby</div>
      <div class="identity-title">Certified Public Accountant</div>
    </div>
    <div class="rule"></div>
    <div class="contact-band">
      <div class="contact-online">
        <div>F. (888) 555-0199</div>
        <div>E. dtwthecpa@ledgerpost.com</div>
        <div>W. harborfilingreliefexperts.com</div>
      </div>
      <div class="contact-address">
        <div>L. 38-27 52nd Street</div>
        <div class="indent">Sunnyside, NY 11287</div>
        <div>T. (718) 555-0142</div>
      </div>
    </div>
  </section>

  <section class="card card-back" aria-label="Business card back">
    <div class="monogram-area" role="img" aria-label="Faint initials monogram watermark"></div>
    <div class="identity">
      <div class="identity-name">Dorian T Welsby</div>
      <div class="identity-title">Certified Public Accountant</div>
    </div>
  </section>
</body>
</html>
```